Fall Event Advertisement for Hearthside Magazine

I will be taking out an ad in Hearthside Magazine to promote the fall events in our community. The audience is middle to upper class, primarily women, looking for fun activities and weekend getaways. The add should include our logo, contact info, a heading, like Discover Brightwater County Fall Festivals & Events or something like that. I appreciate the creativity with the copy.

I have uploaded some photos. They all do not need to be used.

Contact info: Brightwater Chamber of Commerce & Tourism
417 N Alder Ave
Whiteville, NC 28519
(910) 555-0187
For a full listing of year-round events, check out our calendar here, www.thebrightwaterchamber.example

Ad size: 8.25 inches x 10.875 inches

```html
<!DOCTYPE html>
<html lang="en">
<head>
<meta charset="utf-8">
<title>Discover Brightwater County Fall Festivals &amp; Events</title>
<link href="https://fonts.googleapis.com/css2?family=Poppins:wght@400;600;700&display=swap" rel="stylesheet">
<style>
  :root {
    --royal: #283b96;
    --royal-deep: #1f2f82;
    --royal-light: #3c52b0;
    --hat: #c9cfe6;
    --brass: #b89a5c;
    --skin: #5a3f5e;
    --white: #ffffff;
    --ink: #1d1d1f;
    --sky: #1fa3dc;
    --orange: #f7941d;
    --green: #3db54a;
    --rule: rgba(255,255,255,0.35);
  }
  * { margin: 0; padding: 0; box-sizing: border-box; }
  html, body { width: 910px; height: 1200px; overflow: hidden; background: var(--white); }
  body { font-family: "Poppins", sans-serif; color: var(--white); }
  .ad { position: relative; width: 910px; height: 1200px; overflow: hidden; background: var(--white); }

  .hero-photo {
    position: absolute; left: 0; top: 0; width: 910px; height: 1093px;
    background:
      radial-gradient(ellipse 130px 110px at 625px 300px, var(--hat) 0%, rgba(201,207,230,0.5) 45%, transparent 75%),
      radial-gradient(ellipse 110px 55px at 150px 320px, var(--brass) 0%, transparent 75%),
      radial-gradient(ellipse 210px 40px at 330px 410px, rgba(184,154,92,0.75) 0%, transparent 75%),
      radial-gradient(ellipse 80px 90px at 560px 440px, var(--skin) 0%, transparent 75%),
      radial-gradient(ellipse 300px 280px at 560px 700px, var(--royal-light) 0%, transparent 72%),
      linear-gradient(180deg, var(--royal) 0%, var(--royal-deep) 100%);
  }

  .accent-bar { position: absolute; left: 0; top: 62px; width: 8px; height: 77px; background: var(--sky); }

  .headline { position: absolute; left: 0; top: 0; width: 100%; }
  .headline span { position: absolute; white-space: nowrap; line-height: 1; }
  .headline .discover { left: 50px; top: 36px; font-size: 100px; font-weight: 600; letter-spacing: -3px; }
  .headline .county { left: 54px; top: 150px; font-size: 35px; font-weight: 700; letter-spacing: -0.5px; }
  .headline .festivals { left: 50px; top: 182px; font-size: 100px; font-weight: 600; letter-spacing: -3px; }
  .headline .amp { left: 238px; top: 308px; font-size: 30px; font-weight: 600; }
  .headline .events { left: 290px; top: 288px; font-size: 98px; font-weight: 600; letter-spacing: -3px; }

  .brand { position: absolute; right: 58px; top: 52px; text-align: right; }
  .brand .mark { width: 58px; height: 58px; border-radius: 50%; background: var(--sky); margin: 0 38px 22px auto; }
  .brand .name { font-size: 19px; font-weight: 700; line-height: 1; letter-spacing: -0.2px; }
  .brand .sub { font-size: 12px; font-weight: 400; letter-spacing: 3.2px; margin-top: 3px; line-height: 1; }

  .events-panel { position: absolute; left: 55px; top: 739px; width: 799px; height: 294px; border: 1px solid var(--rule); }
  .events-panel .divider { position: absolute; left: 350px; top: 26px; width: 1px; height: 238px; background: var(--rule); }
  .column { position: absolute; top: 28px; }
  .column.left { left: 25px; width: 296px; }
  .column.right { left: 383px; width: 390px; }
  .event { height: 80px; font-size: 14.2px; line-height: 20px; font-weight: 400; }
  .event + .event { border-top: 1px solid var(--rule); padding-top: 11px; }
  .event:first-child { height: 70px; }
  .event h3 { font-size: 14.2px; font-weight: 700; line-height: 20px; white-space: nowrap; }
  .event h3 .sep { font-weight: 400; opacity: 0.7; margin: 0 4px; }
  .event p { white-space: nowrap; }

  .color-band { position: absolute; left: 0; top: 1093px; width: 910px; height: 5px; display: flex; }
  .color-band i { flex: 1; }
  .color-band .o { background: var(--orange); }
  .color-band .g { background: var(--green); }
  .color-band .b { background: var(--sky); }

  .footer { position: absolute; left: 0; top: 1098px; width: 910px; height: 102px; color: var(--ink); }
  .footer .address { position: absolute; left: 40px; width: 175px; top: 30px; text-align: center; font-size: 13.5px; line-height: 18.5px; }
  .footer .contact { position: absolute; left: 305px; width: 160px; top: 31px; text-align: center; }
  .footer .label { color: var(--sky); font-size: 10px; line-height: 14px; }
  .footer .phone { font-size: 16px; line-height: 22px; margin-top: 3px; }
  .footer .web { position: absolute; right: 56px; top: 31px; text-align: right; }
  .footer .web .url { font-size: 14.5px; line-height: 20px; margin-top: 4px; text-align: center; }
</style>
</head>
<body>
<div class="ad">
  <div class="hero-photo" role="img" aria-label="Photo of a marching band trumpeter in a blue and white uniform and white plumed hat, playing a brass trumpet, tinted royal blue"></div>
  <div class="accent-bar"></div>

  <h1 class="headline">
    <span class="discover">Discover</span>
    <span class="county">Brightwater County Fall</span>
    <span class="festivals">Festivals</span>
    <span class="amp">&amp;</span>
    <span class="events">Events</span>
  </h1>

  <div class="brand">
    <div class="mark"></div>
    <div class="name">BRIGHTWATER CHAMBER</div>
    <div class="sub">OF COMMERCE &amp; TOURISM</div>
  </div>

  <section class="events-panel">
    <div class="divider"></div>
    <div class="column left">
      <div class="event">
        <h3>Lakeside Tri Days<span class="sep">|</span>Sept 2-4</h3>
        <p>Lake Waccamaw, NC</p>
        <p>Run – Bike – Swim – Paddle</p>
      </div>
      <div class="event">
        <h3>Harvest Stew Festival<span class="sep">|</span>Sept 24</h3>
        <p>Brunswick, NC</p>
        <p>Parade – Family Fun – Good Eats</p>
      </div>
      <div class="event">
        <h3>Brightwater County Agricultural Fair</h3>
        <p>Whiteville, NC</p>
        <p>Carnival Rides – Tractor Pull</p>
        <p>– Demolition Derby – Live Entertainment</p>
      </div>
    </div>
    <div class="column right">
      <div class="event">
        <h3>Sweet Potato Jubilee<span class="sep">|</span>Oct 22</h3>
        <p>Tabor City, NC</p>
        <p>Arts &amp; Crafts – Parade – Food - Entertainment</p>
      </div>
      <div class="event">
        <h3>Pecan Harvest Days<span class="sep">|</span>Nov 4-5</h3>
        <p>Whiteville, NC</p>
        <p>Car Show – Entertainment – Burger Brawl – Beer Garden</p>
      </div>
      <div class="event">
        <h3>Autumn Heritage Pow Wow<span class="sep">|</span>Oct 15-16</h3>
        <p>Buckhead, NC</p>
        <p>Traditional Foods - History – American Indian</p>
        <p>Dance &amp; Drumming Competition</p>
      </div>
    </div>
  </section>

  <div class="color-band">
    <i class="o"></i><i class="g"></i><i class="b"></i><i class="o"></i><i class="g"></i><i class="b"></i>
  </div>

  <footer class="footer">
    <div class="address">417 N Alder Ave<br>Whiteville, NC 28519</div>
    <div class="contact">
      <div class="label">Contact us at:</div>
      <div class="phone">910-555-0187</div>
    </div>
    <div class="web">
      <div class="label">For a full listing of year-round events, check out our calendar here</div>
      <div class="url">www.thebrightwaterchamber.example</div>
    </div>
  </footer>
</div>
</body>
</html>
```